Innovation Presentation Template

I need a unique template design for a presentation on Innovation used exclusively inside of our company. I'd prefer to work in Apple Keynote but can take a .ppt and convert it. The template should appeal to a broad audience of diverse job descriptions. This is a one-time presentation that will last between 30 and 45 minutes. The design should provide a strong visual appeal with multiple chart layouts to support highlighted test points (no bullets, I hate bullets), graphics, line art, and video/photos. My presentations are sparse, never more that 2 concepts per chart (usually one). Our company is a high tech manufacturer selling products in many markets ranging from Government to consumer. The final design should include style a style guide including suggested fonts, colors, graph formats, suggested word art, etc.

Target Market(s)

The audience is internal employees only. Strong corporate branding is not required in this presentation.

Industry/Entity Type

Government

Colors
3277b5
faa54b

Requirements
Must have
• Strong visual appeal helping to support the communication of simple concepts (that have been broken down from complex subject matter).

Multiple chart template forms to support different forms of communication including text points, data charts, graphics, photos, and videos.

Visuals will be memorable, but not overpower the content. Visuals will help convey the content.

Well conceived and coordinated color pallets. Fonts guides (that I can access).

You can visit our company web site at www.KOVEX.com to see logo and corporate look/feel. It would be good to build logo into a few of the chart templates, but not all.
Nice to have
• Keynote (please). I can live with .ppt if I have to.

Many charts will make a point with simple single sentences. Find a way to make the sentences graphically interesting by varying font and/or color of specific words to help drive points.

Note that colors that I've identified below are based upon the blue used in our logo and the orange that complements it. I'm not married to these but use them as guidelines.
Should not have
• Noise. Corporate nauseia.

```html
<!DOCTYPE html>
<html lang="en">
<head>
<meta charset="utf-8">
<title>Innovation Presentation Template – Slide Overview</title>
<link rel="stylesheet" href="https://fonts.googleapis.com/css2?family=Open+Sans:wght@300;400;600;700&family=Roboto+Slab:wght@500;700&display=swap">
<style>
:root{
  --blue:#3277b5;
  --blue-dark:#2a6399;
  --orange:#faa54b;
  --orange-deep:#e8772e;
  --red:#e5532d;
  --teal:#1ba1c9;
  --ink:#4a4a4a;
  --ink-dark:#333;
  --grey:#a5a5a5;
  --grey-light:#e6e6e6;
  --grey-line:#d5d5d5;
  --band:#4d4d4d;
  --page:#ececec;
  --white:#fff;
}
*{box-sizing:border-box;margin:0;padding:0}
html,body{width:1050px;height:1200px;overflow:hidden}
body{background:var(--page);font-family:"Open Sans",Arial,sans-serif;color:var(--ink);position:relative}
.slide{position:absolute;width:300px;height:226px;background:var(--white);overflow:hidden;box-shadow:0 1px 4px rgba(0,0,0,.18)}
.c1{left:55px}.c2{left:375px}.c3{left:695px}
.r1{top:5px}.r2{top:246px}.r3{top:483px}.r4{top:722px}.r5{top:959px}
.slide-title{position:absolute;left:9px;top:6px;font-family:"Roboto Slab",Georgia,serif;font-weight:700;font-size:12.5px;color:var(--blue)}
.slide-sub{position:absolute;left:9px;top:22px;font-size:7px;color:var(--orange)}
.slide-num{position:absolute;right:9px;top:4px;width:15px;height:15px;background:var(--blue);color:var(--white);font-size:8px;font-weight:700;text-align:center;line-height:15px}
.footer{position:absolute;left:0;right:0;bottom:0;height:22px}
.footer .logo{position:absolute;left:8px;top:2px;font-size:12px;color:var(--blue);font-weight:300}
.footer .rule{position:absolute;left:34px;right:60px;top:12px;height:1px;background:var(--grey-line)}
.footer .site{position:absolute;left:0;right:0;top:7px;text-align:center;font-size:4px;color:var(--ink)}
.footer .pager{position:absolute;right:8px;top:6px;width:48px;height:10px;border-radius:5px;background:var(--grey-light);font-size:4.5px;line-height:10px;display:flex;justify-content:space-around}
.pager .next{color:var(--red)}
.lorem{font-size:5.3px;line-height:1.35;color:var(--ink)}
.kicker{font-size:8.5px;color:var(--orange-deep);letter-spacing:.1px}
.ph{position:absolute;display:flex;align-items:center;justify-content:center}
.ph svg{display:block}
.orange-box{background:var(--orange)}

/* 1 cover */
.cover-photo{position:absolute;inset:0;background:linear-gradient(135deg,#cfe3ee 0%,#8fb4cb 35%,#34404e 60%,#d8dde2 100%)}
.cover-band{position:absolute;left:0;right:0;top:172px;height:42px;background:rgba(50,119,181,.92)}
.cover-title{position:absolute;left:8px;top:178px;color:var(--white);font-size:24px;font-weight:300}

/* 3 image & text */
.bokeh{position:absolute;left:0;top:0;bottom:0;width:150px;background:radial-gradient(circle at 80% 10%,#f5a623 0,#c86a1a 18%,transparent 40%),radial-gradient(circle at 30% 70%,#2aa0e6 0,#1a5fa8 25%,transparent 55%),linear-gradient(160deg,#0a1f4a,#0b2d6b 50%,#061538)}
.it-title{position:absolute;left:161px;top:42px;font-family:"Roboto Slab",Georgia,serif;font-weight:700;font-size:12.5px;color:var(--blue)}
.it-sub{position:absolute;left:161px;top:58px;font-size:7px;color:var(--orange)}

/* 4 left column */
.quote{position:absolute;left:18px;top:60px;width:82px;text-align:center;font-size:6px;line-height:1.4}
.quote .mark{display:block;font-size:12px;color:var(--grey);line-height:1}
.col-rule{position:absolute;left:106px;top:62px;width:1px;height:112px;background:var(--grey-line)}

/* 5 icons */
.icon-tile{position:absolute;top:49px;width:39px;height:39px;background:var(--orange);display:flex;align-items:center;justify-content:center}
.icon-label{position:absolute;top:106px;width:80px;text-align:center;font-size:8px;color:var(--orange-deep);font-weight:600}
.icon-text{position:absolute;top:118px;width:80px;text-align:center}

/* 6 team */
.member{position:absolute;top:34px;width:70px;height:160px;background:var(--blue)}
.member .name{position:absolute;left:0;right:0;top:86px;height:12px;background:var(--blue-dark);color:var(--white);font-size:5.5px;font-weight:700;line-height:12px;padding-left:3px;display:flex;justify-content:space-between;padding-right:3px}
.member .lorem{position:absolute;left:3px;right:3px;top:110px;color:var(--white);font-size:5px}

/* 8 table */
.dark-band{position:absolute;left:0;right:0;top:48px;height:31px;background:var(--band);color:var(--white);font-size:5.5px;line-height:1.35;text-align:center;padding:6px 10px}
.data-table{position:absolute;left:30px;top:89px;width:240px;border-collapse:collapse;font-size:5px;color:var(--ink)}
.data-table th{background:var(--teal);color:var(--white);font-weight:400;height:14px}
.data-table td{height:15px;text-align:center;border-top:1px solid var(--white)}
.data-table td:first-child{text-align:left;padding-left:8px}
.data-table tr:nth-child(odd) td{background:#dcdcdc}
.data-table tr:nth-child(even) td{background:#ececec}
.data-table th.hi{background:var(--blue)}
.data-table td.hi{background:#5aa9dc!important;color:var(--white)}
.data-table tr:nth-child(even) td.hi{background:#7fbfe6!important}

/* 9 bullets */
.bullet{position:absolute;left:24px;width:255px}
.bullet::before{content:"";position:absolute;left:-9px;top:2px;width:5px;height:5px;border-radius:50%;background:var(--red)}
.sub-bullet{position:absolute;left:50px;width:230px}
.sub-bullet::before{content:"-";position:absolute;left:-7px;top:0}

/* legend blocks */
.legend-item{position:absolute;left:160px;width:125px;padding-left:8px}
.legend-item::before{content:"";position:absolute;left:0;top:1px;width:4px;height:32px;background:var(--c)}

/* 13 timeline */
.tl-text{position:absolute;font-size:4.6px;line-height:1.3;width:38px}
.tl-num{position:absolute;font-size:7.5px;color:var(--ink)}
.tl-num.o{color:var(--orange)}

/* 14 thank you */
.thanks{background:var(--blue)}
.thanks h2{position:absolute;left:14px;top:125px;font-weight:300;font-size:19px;color:var(--white);letter-spacing:.5px}
.thanks .under{position:absolute;left:14px;top:148px;width:110px;height:1px;background:rgba(255,255,255,.7)}
.contact{position:absolute;left:20px;display:flex;align-items:center;gap:10px;font-size:5px;color:var(--white)}
.social{position:absolute;left:18px;top:207px;display:flex;gap:6px}
.social span{width:9px;height:9px;background:var(--white);opacity:.9}
</style>
</head>
<body>

<!-- 1 Cover -->
<section class="slide c1 r1">
  <div class="cover-photo" role="img" aria-label="Photo of a business team meeting around a white table in a bright office"></div>
  <div class="cover-band"></div>
  <h1 class="cover-title">Presentation Title</h1>
</section>

<!-- 2 About Us -->
<section class="slide c2 r1">
  <h2 class="slide-title">About Us</h2><p class="slide-sub">text &nbsp;for second title</p><span class="slide-num">2</span>
  <p class="kicker" style="position:absolute;left:14px;top:62px;border-bottom:1px solid var(--orange);padding-bottom:2px">LOREM IPSUM DOLOR SIT AMET</p>
  <p class="lorem" style="position:absolute;left:14px;top:78px;width:125px">Lorem ipsum dolor sit amet, consectetur adipiscing elit. Aliquam odio nulla, blandit eu suscipit ac, pulvinar in mauris. Mauris ac sodales ante. Donec congue lectus vel libero facilisis luctus. Lorem ipsum dolor sit amet, consectetur adipiscing elit. Aliquam odio nulla, blandit eu suscipit ac, pulvinar in mauris. Mauris ac sodales ante. Donec congue lectus vel libero facilisis luctus. Lorem ipsum dolor sit amet, consectetur adipiscing elit. Aliquam odio nulla, blandit eu suscipit ac, pulvinar in mauris. Mauris ac sodales ante. Donec congue lectus vel libero facilisis luctus.</p>
  <div class="ph orange-box" style="left:140px;top:58px;width:138px;height:126px" role="img" aria-label="Image placeholder">
    <svg width="64" height="52" viewBox="0 0 64 52" fill="none" stroke="#fff" stroke-width="3"><rect x="2" y="8" width="38" height="30" rx="3" transform="rotate(-12 21 23)"/><rect x="18" y="14" width="42" height="34" rx="3" fill="#faa54b"/><path d="M21 44l12-14 8 9 6-6 10 11"/><circle cx="48" cy="23" r="3"/></svg>
  </div>
  <footer class="footer"><span class="logo">logo</span><span class="rule"></span><span class="site">www.yourwebsite.com</span><span class="pager"><span class="next">Next</span><span>Previous</span></span></footer>
</section>

<!-- 3 Image & Texts -->
<section class="slide c3 r1">
  <span class="slide-num">3</span>
  <div class="bokeh" role="img" aria-label="Abstract blue and orange bokeh light image"></div>
  <h2 class="it-title">Image &amp; Texts</h2><p class="it-sub">text &nbsp;for second title</p>
  <p class="lorem" style="position:absolute;left:161px;top:74px;width:128px">Lorem ipsum dolor sit amet, consectetur adipiscing elit. Aliquam odio nulla, blandit eu suscipit ac, pulvinar in mauris. Mauris ac sodales ante. Donec congue lectus vel libero facilisis luctus. Lorem ipsum dolor sit amet, consectetur adipiscing elit. Aliquam odio nulla, blandit eu suscipit ac, pulvinar in mauris. Mauris ac sodales ante. Donec congue lectus vel libero facilisis luctus. Lorem ipsum dolor sit amet, consectetur adipiscing elit. Aliquam odio nulla, blandit eu suscipit ac, pulvinar in mauris. Mauris ac sodales ante. Donec congue lectus vel libero facilisis luctus.</p>
</section>

<!-- 4 Left Column Style -->
<section class="slide c1 r2">
  <h2 class="slide-title">Left Column Style</h2><p class="slide-sub">text &nbsp;for second title</p><span class="slide-num">4</span>
  <blockquote class="quote"><span class="mark">&ldquo;</span><b>Lorem ipsum dolor sit amet,</b> consectetur adipiscing elit. Aliquam odio nulla, blandit eu suscipit ac, pulvinar in mauris. Mauris ac sodales ante. Donec congue lectus vel libero facilisis luctus.<span class="mark">&rdquo;</span></blockquote>
  <span class="col-rule"></span>
  <p class="kicker" style="position:absolute;left:120px;top:52px">LOREM IPSUM DOLOR SIT AMET</p>
  <p class="lorem" style="position:absolute;left:120px;top:66px;width:165px">Lorem ipsum dolor sit amet, consectetur adipiscing elit. Aliquam odio nulla, blandit eu suscipit ac, pulvinar in mauris. Mauris ac sodales ante. Donec congue lectus vel libero facilisis luctus.<br><br>Lorem ipsum dolor sit amet, consectetur adipiscing elit. Aliquam odio nulla, blandit eu suscipit ac, pulvinar in mauris. Mauris ac sodales ante. Donec congue lectus vel libero facilisis luctus.<br><br>Lorem ipsum dolor sit amet, consectetur adipiscing elit. Aliquam odio nulla, blandit eu suscipit ac, pulvinar in mauris. Mauris ac sodales ante. Donec congue lectus vel libero facilisis luctus.</p>
  <footer class="footer"><span class="logo">logo</span><span class="rule"></span><span class="site">www.yourwebsite.com</span><span class="pager"><span class="next">Next</span><span>Previous</span></span></footer>
</section>

<!-- 5 Iconic Style -->
<section class="slide c2 r2">
  <h2 class="slide-title">Iconic Style</h2><p class="slide-sub">text &nbsp;for second title</p><span class="slide-num">5</span>
  <div class="icon-tile" style="left:37px"><svg width="20" height="18" viewBox="0 0 20 18" fill="none" stroke="#fff" stroke-width="1.8"><path d="M1 2h3l3 10h9l2-7H6"/><circle cx="8" cy="15.5" r="1.4" fill="#fff"/><circle cx="15" cy="15.5" r="1.4" fill="#fff"/></svg></div>
  <div class="icon-tile" style="left:124px"><svg width="20" height="20" viewBox="0 0 20 20" fill="#fff"><circle cx="7" cy="5" r="3"/><path d="M1 18v-5a4 4 0 0 1 4-4h4a4 4 0 0 1 4 4v5z"/><rect x="12" y="2" width="7" height="6"/></svg></div>
  <div class="icon-tile" style="left:211px"><svg width="20" height="20" viewBox="0 0 20 20" fill="none" stroke="#fff" stroke-width="1.6"><circle cx="10" cy="9" r="4.5"/><path d="M8 15h4M8.5 17.5h3M10 1v1.5M3 9H1.5M18.5 9H17M4.5 3.5l1 1M15.5 3.5l-1 1"/></svg></div>
  <p class="icon-label" style="left:17px">Lorem ipsum</p><p class="icon-label" style="left:104px">Lorem ipsum</p><p class="icon-label" style="left:191px">Lorem ipsum</p>
  <p class="lorem icon-text" style="left:17px">Lorem ipsum dolor sit amet, consectetur adipiscing elit. Aliquam odio nulla, blandit eu suscipit ac, pulvinar in mauris. Mauris ac sodales ante. Donec congue lectus vel libero facilisis luctus.</p>
  <p class="lorem icon-text" style="left:104px">Lorem ipsum dolor sit amet, consectetur adipiscing elit. Aliquam odio nulla, blandit eu suscipit ac, pulvinar in mauris. Mauris ac sodales ante. Donec congue lectus vel libero facilisis luctus.</p>
  <p class="lorem icon-text" style="left:191px">Lorem ipsum dolor sit amet, consectetur adipiscing elit. Aliquam odio nulla, blandit eu suscipit ac, pulvinar in mauris. Mauris ac sodales ante. Donec congue lectus vel libero facilisis luctus.</p>
  <footer class="footer"><span class="logo">logo</span><span class="rule"></span><span class="site">www.yourwebsite.com</span><span class="pager"><span class="next">Next</span><span>Previous</span></span></footer>
</section>

<!-- 6 The Team -->
<section class="slide c3 r2">
  <h2 class="slide-title" style="top:2px">The Team</h2><p class="slide-sub" style="top:17px">text &nbsp;for second title</p><span class="slide-num">6</span>
  <div class="member" style="left:7px"><div class="ph" style="left:0;right:0;top:12px;height:60px" role="img" aria-label="Team member photo placeholder"><svg width="46" height="38" viewBox="0 0 64 52" fill="none" stroke="#fff" stroke-width="3"><rect x="2" y="8" width="38" height="30" rx="3" transform="rotate(-12 21 23)"/><rect x="18" y="14" width="42" height="34" rx="3" fill="#3277b5"/><path d="M21 44l12-14 8 9 6-6 10 11"/><circle cx="48" cy="23" r="3"/></svg></div><div class="name"><span>John Doe</span><span>Manager</span></div><p class="lorem">Lorem ipsum dolor sit amet, consectetur adipiscing elit. Aliquam odio nulla, blandit eu suscipit ac, pulvinar in mauris. Mauris ac sodales ante. Donec congue lectus vel libero facilisis luctus.</p></div>
  <div class="member" style="left:78px"><div class="ph" style="left:0;right:0;top:12px;height:60px" role="img" aria-label="Team member photo placeholder"><svg width="46" height="38" viewBox="0 0 64 52" fill="none" stroke="#fff" stroke-width="3"><rect x="2" y="8" width="38" height="30" rx="3" transform="rotate(-12 21 23)"/><rect x="18" y="14" width="42" height="34" rx="3" fill="#3277b5"/><path d="M21 44l12-14 8 9 6-6 10 11"/><circle cx="48" cy="23" r="3"/></svg></div><div class="name"><span>John Doe</span><span>Manager</span></div><p class="lorem">Lorem ipsum dolor sit amet, consectetur adipiscing elit. Aliquam odio nulla, blandit eu suscipit ac, pulvinar in mauris. Mauris ac sodales ante. Donec congue lectus vel libero facilisis luctus.</p></div>
  <div class="member" style="left:149px"><div class="ph" style="left:0;right:0;top:12px;height:60px" role="img" aria-label="Team member photo placeholder"><svg width="46" height="38" viewBox="0 0 64 52" fill="none" stroke="#fff" stroke-width="3"><rect x="2" y="8" width="38" height="30" rx="3" transform="rotate(-12 21 23)"/><rect x="18" y="14" width="42" height="34" rx="3" fill="#3277b5"/><path d="M21 44l12-14 8 9 6-6 10 11"/><circle cx="48" cy="23" r="3"/></svg></div><div class="name"><span>John Doe</span><span>Manager</span></div><p class="lorem">Lorem ipsum dolor sit amet, consectetur adipiscing elit. Aliquam odio nulla, blandit eu suscipit ac, pulvinar in mauris. Mauris ac sodales ante. Donec congue lectus vel libero facilisis luctus.</p></div>
  <div class="member" style="left:220px;width:73px"><div class="ph" style="left:0;right:0;top:12px;height:60px" role="img" aria-label="Team member photo placeholder"><svg width="46" height="38" viewBox="0 0 64 52" fill="none" stroke="#fff" stroke-width="3"><rect x="2" y="8" width="38" height="30" rx="3" transform="rotate(-12 21 23)"/><rect x="18" y="14" width="42" height="34" rx="3" fill="#3277b5"/><path d="M21 44l12-14 8 9 6-6 10 11"/><circle cx="48" cy="23" r="3"/></svg></div><div class="name"><span>John Doe</span><span>Manager</span></div><p class="lorem">Lorem ipsum dolor sit amet, consectetur adipiscing elit. Aliquam odio nulla, blandit eu suscipit ac, pulvinar in mauris. Mauris ac sodales ante. Donec congue lectus vel libero facilisis luctus.</p></div>
  <footer class="footer"><span class="logo">logo</span><span class="rule"></span><span class="site">www.yourwebsite.com</span><span class="pager"><span class="next">Next</span><span>Previous</span></span></footer>
</section>

<!-- 7 Team Member -->
<section class="slide c1 r3">
  <h2 class="slide-title">Team Member</h2><p class="slide-sub">text &nbsp;for second title</p><span class="slide-num">7</span>
  <div class="ph orange-box" style="left:7px;top:43px;width:77px;height:82px" role="img" aria-label="Team member photo placeholder"><svg width="52" height="42" viewBox="0 0 64 52" fill="none" stroke="#fff" stroke-width="3"><rect x="2" y="8" width="38" height="30" rx="3" transform="rotate(-12 21 23)"/><rect x="18" y="14" width="42" height="34" rx="3" fill="#faa54b"/><path d="M21 44l12-14 8 9 6-6 10 11"/><circle cx="48" cy="23" r="3"/></svg></div>
  <svg style="position:absolute;left:8px;top:133px" width="60" height="40" viewBox="0 0 60 40"><circle cx="4" cy="4" r="4" fill="#e8772e"/><circle cx="4" cy="19" r="4" fill="#e8772e"/><circle cx="4" cy="34" r="4" fill="#e8772e"/><text x="12" y="6.5" font-size="7" fill="#4a4a4a" font-family="Open Sans,sans-serif">lorem ipsum</text><text x="12" y="21.5" font-size="7" fill="#4a4a4a" font-family="Open Sans,sans-serif">lorem ipsum</text><text x="12" y="36.5" font-size="7" fill="#4a4a4a" font-family="Open Sans,sans-serif">lorem ipsum</text></svg>
  <p class="kicker" style="position:absolute;left:99px;top:43px;color:var(--red)">LOREM IPSUM DOLOR SIT AMET</p>
  <p style="position:absolute;left:99px;top:55px;font-size:6.5px">lorem ipsum dolor sit amet</p>
  <p class="lorem" style="position:absolute;left:99px;top:70px;width:190px">Lorem ipsum dolor sit amet, consectetur adipiscing elit. Aliquam odio nulla, blandit eu suscipit ac, pulvinar in mauris. Mauris ac sodales ante. Donec congue lectus vel libero facilisis luctus.<br><br>Lorem ipsum dolor sit amet, consectetur adipiscing elit. Aliquam odio nulla, blandit eu suscipit ac, pulvinar in mauris. Mauris ac sodales ante. Donec congue lectus vel libero facilisis luctus.<br><br>Lorem ipsum dolor sit amet, consectetur adipiscing elit. Aliquam odio nulla, blandit eu suscipit ac, pulvinar in mauris. Mauris ac sodales ante. Donec congue lectus vel libero facilisis luctus.</p>
  <footer class="footer"><span class="logo">logo</span><span class="rule"></span><span class="site">www.yourwebsite.com</span><span class="pager"><span class="next">Next</span><span>Previous</span></span></footer>
</section>

<!-- 8 Table Slide -->
<section class="slide c2 r3">
  <h2 class="slide-title">Table Slide</h2><p class="slide-sub">text &nbsp;for second title</p><span class="slide-num">8</span>
  <p class="dark-band">Lorem ipsum dolor sit amet, consectetur adipiscing elit. Aliquam odio nulla, blandit eu suscipit ac, pulvinar in mauris. Mauris ac sodales ante. Donec congue lectus vel libero facilisis luctus.</p>
  <table class="data-table">
    <thead><tr><th>LOREM IPSUM</th><th>LOREM IPSUM</th><th>LOREM IPSUM</th><th class="hi">LOREM IPSUM</th></tr></thead>
    <tbody>
      <tr><td>LOREM IPSUM</td><td>01</td><td>02</td><td class="hi">03</td></tr>
      <tr><td>LOREM IPSUM</td><td>04</td><td>05</td><td class="hi">06</td></tr>
      <tr><td>LOREM IPSUM</td><td>07</td><td>08</td><td class="hi">09</td></tr>
      <tr><td>LOREM IPSUM</td><td>10</td><td>11</td><td class="hi">12</td></tr>
      <tr><td>LOREM IPSUM</td><td>13</td><td>14</td><td class="hi">15</td></tr>
    </tbody>
  </table>
  <footer class="footer"><span class="logo">logo</span><span class="rule"></span><span class="site">www.yourwebsite.com</span><span class="pager"><span class="next">Next</span><span>Previous</span></span></footer>
</section>

<!-- 9 Bulletins Style -->
<section class="slide c3 r3">
  <h2 class="slide-title">Bulletins Style</h2><p class="slide-sub">text &nbsp;for second title</p><span class="slide-num">8</span>
  <p class="lorem bullet" style="top:46px">Lorem ipsum dolor sit amet, consectetur adipiscing elit. Aliquam odio nulla, blandit eu suscipit ac, pulvinar in mauris. Mauris ac sodales ante. Donec congue lectus vel libero facilisis luctus.</p>
  <p class="lorem sub-bullet" style="top:78px">Lorem ipsum dolor sit amet, consectetur adipiscing elit. Aliquam odio nulla, blandit eu suscipit ac, pulvinar in mauris. Mauris ac sodales ante.</p>
  <p class="lorem sub-bullet" style="top:98px">Lorem ipsum dolor sit amet, consectetur adipiscing elit. Aliquam odio nulla, blandit eu suscipit ac, pulvinar in mauris. Mauris ac sodales ante.</p>
  <p class="lorem bullet" style="top:124px">Lorem ipsum dolor sit amet, consectetur adipiscing elit. Aliquam odio nulla, blandit eu suscipit ac, pulvinar in mauris. Mauris ac sodales ante. Donec congue lectus vel libero facilisis luctus.</p>
  <p class="lorem bullet" style="top:152px">Lorem ipsum dolor sit amet, consectetur adipiscing elit. Aliquam odio nulla, blandit eu suscipit ac, pulvinar in mauris. Mauris ac sodales ante. Donec congue lectus vel libero facilisis luctus.</p>
  <footer class="footer"><span class="logo">logo</span><span class="rule"></span><span class="site">www.yourwebsite.com</span><span class="pager"><span class="next">Next</span><span>Previous</span></span></footer>
</section>

<!-- 10 Line chart -->
<section class="slide c1 r4">
  <h2 class="slide-title">Graphic Chart Style</h2><p class="slide-sub">text &nbsp;for second title</p><span class="slide-num">9</span>
  <svg style="position:absolute;left:0;top:0" width="300" height="226" viewBox="0 0 300 226" font-family="Open Sans,sans-serif" font-size="4">
    <g stroke="#e4e4e4" stroke-width=".5">
      <line x1="60" y1="62" x2="215" y2="62"/><line x1="60" y1="72" x2="215" y2="72"/><line x1="60" y1="82" x2="215" y2="82"/><line x1="60" y1="92" x2="215" y2="92"/><line x1="60" y1="102" x2="215" y2="102"/><line x1="60" y1="112" x2="215" y2="112"/><line x1="60" y1="122" x2="215" y2="122"/><line x1="60" y1="132" x2="215" y2="132"/><line x1="60" y1="142" x2="215" y2="142"/><line x1="60" y1="152" x2="215" y2="152"/><line x1="60" y1="162" x2="215" y2="162"/>
    </g>
    <g fill="#666" text-anchor="end">
      <text x="57" y="63">10,000,000</text><text x="57" y="73">9,000,000</text><text x="57" y="83">8,000,000</text><text x="57" y="93">7,000,000</text><text x="57" y="103">6,000,000</text><text x="57" y="113">5,000,000</text><text x="57" y="123">4,000,000</text><text x="57" y="133">3,000,000</text><text x="57" y="143">2,000,000</text><text x="57" y="153">1,000,000</text><text x="57" y="168">(1,000,000)</text>
    </g>
    <text x="32" y="112" fill="#666" transform="rotate(-90 32 112)">US $</text>
    <g fill="#666" text-anchor="middle"><text x="73" y="169">Year 1</text><text x="100" y="169">Year 2</text><text x="127" y="169">Year 3</text><text x="154" y="169">Year 4</text><text x="182" y="169">Year 5</text></g>
    <polyline points="73,145 100,136 127,118 154,92 182,64" fill="none" stroke="#3277b5" stroke-width="1.2"/>
    <polyline points="73,153 100,150 127,146 154,138 182,124" fill="none" stroke="#faa54b" stroke-width="1.2"/>
    <polyline points="73,156 100,155 127,153 154,149 182,144" fill="none" stroke="#333" stroke-width="1.2"/>
    <g fill="#3277b5"><circle cx="73" cy="145" r="1.2"/><circle cx="100" cy="136" r="1.2"/><circle cx="127" cy="118" r="1.2"/><circle cx="154" cy="92" r="1.2"/><circle cx="182" cy="64" r="1.2"/></g>
    <g fill="#faa54b"><circle cx="73" cy="153" r="1.2"/><circle cx="100" cy="150" r="1.2"/><circle cx="127" cy="146" r="1.2"/><circle cx="154" cy="138" r="1.2"/><circle cx="182" cy="124" r="1.2"/></g>
    <g fill="#333"><circle cx="73" cy="156" r="1.2"/><circle cx="100" cy="155" r="1.2"/><circle cx="127" cy="153" r="1.2"/><circle cx="154" cy="149" r="1.2"/><circle cx="182" cy="144" r="1.2"/></g>
    <g fill="#555"><line x1="220" y1="96" x2="228" y2="96" stroke="#3277b5"/><text x="230" y="97.5">Total Revenue</text><line x1="220" y1="104" x2="228" y2="104" stroke="#faa54b"/><text x="230" y="105.5">Gross Profit</text><line x1="220" y1="112" x2="228" y2="112" stroke="#333"/><text x="230" y="113.5">Earning After Taxes (EAT)</text></g>
  </svg>
  <footer class="footer"><span class="logo">logo</span><span class="rule"></span><span class="site">www.yourwebsite.com</span><span class="pager"><span class="next">Next</span><span>Previous</span></span></footer>
</section>

<!-- 11 Pie chart -->
<section class="slide c2 r4">
  <h2 class="slide-title">Graphic Chart Style</h2><p class="slide-sub">text &nbsp;for second title</p><span class="slide-num">9</span>
  <svg style="position:absolute;left:0;top:0" width="160" height="226" viewBox="0 0 160 226" font-family="Open Sans,sans-serif" font-size="5">
    <path d="M80 118 L80 70 A48 48 0 1 1 54.3 158.5 Z" fill="#3277b5"/>
    <path d="M80 118 L54.3 158.5 A48 48 0 0 1 36.6 97.6 Z" fill="#faa54b"/>
    <path d="M80 118 L36.6 97.6 A48 48 0 0 1 56.9 75.9 Z" fill="#a5a5a5"/>
    <path d="M80 118 L56.9 75.9 A48 48 0 0 1 80 70 Z" fill="#444"/>
    <text x="131" y="128" fill="#3277b5">1st Qtr</text>
    <text x="8" y="136" fill="#e8772e">2nd Qtr</text>
    <text x="18" y="80" fill="#666">3rd Qtr</text>
    <text x="44" y="64" fill="#e8a53a">4th Qtr</text>
  </svg>
  <p class="lorem legend-item" style="top:48px;--c:#4a4a4a">Lorem ipsum dolor sit amet, consectetur adipiscing elit. Aliquam odio nulla, blandit eu suscipit ac, pulvinar in mauris. Mauris ac sodales ante. Donec congue lectus vel libero facilisis luctus.</p>
  <p class="lorem legend-item" style="top:94px;--c:var(--orange)">Lorem ipsum dolor sit amet, consectetur adipiscing elit. Aliquam odio nulla, blandit eu suscipit ac, pulvinar in mauris. Mauris ac sodales ante. Donec congue lectus vel libero facilisis luctus.</p>
  <p class="lorem legend-item" style="top:140px;--c:var(--red)">Lorem ipsum dolor sit amet, consectetur adipiscing elit. Aliquam odio nulla, blandit eu suscipit ac, pulvinar in mauris. Mauris ac sodales ante. Donec congue lectus vel libero facilisis luctus.</p>
  <footer class="footer"><span class="logo">logo</span><span class="rule"></span><span class="site">www.yourwebsite.com</span><span class="pager"><span class="next">Next</span><span>Previous</span></span></footer>
</section>

<!-- 12 Bar chart -->
<section class="slide c3 r4">
  <h2 class="slide-title">Graphic Chart Style</h2><p class="slide-sub">text &nbsp;for second title</p><span class="slide-num">10</span>
  <svg style="position:absolute;left:0;top:0" width="150" height="226" viewBox="0 0 150 226" font-family="Open Sans,sans-serif" font-size="4.5">
    <line x1="22" y1="168" x2="130" y2="168" stroke="#bbb" stroke-width=".5"/>
    <g fill="#3277b5"><rect x="25" y="145" width="7" height="23"/><rect x="52" y="152" width="7" height="16"/><rect x="79" y="123" width="7" height="45"/><rect x="106" y="146" width="7" height="22"/></g>
    <g fill="#faa54b"><rect x="32" y="64" width="7" height="104"/><rect x="59" y="104" width="7" height="64"/><rect x="86" y="53" width="7" height="115"/><rect x="113" y="97" width="7" height="71"/></g>
    <g fill="#444"><rect x="39" y="108" width="7" height="60"/><rect x="66" y="118" width="7" height="50"/><rect x="93" y="98" width="7" height="70"/><rect x="120" y="144" width="7" height="24"/></g>
    <g fill="#666" text-anchor="middle"><text x="35" y="175">2009</text><text x="62" y="175">2010</text><text x="89" y="175">2011</text><text x="116" y="175">2012</text></g>
    <g fill="#666"><text x="133" y="60">12</text><text x="133" y="77">10</text><text x="133" y="94">8</text><text x="133" y="111">6</text><text x="133" y="128">4</text><text x="133" y="145">2</text><text x="133" y="162">0</text></g>
    <g font-size="3.5"><rect x="22" y="181" width="4" height="4" fill="#444"/><text x="28" y="184" fill="#444">Description</text><rect x="54" y="181" width="4" height="4" fill="#3277b5"/><text x="60" y="184" fill="#3277b5">Description</text><rect x="86" y="181" width="4" height="4" fill="#e5532d"/><text x="92" y="184" fill="#e5532d">Description</text></g>
  </svg>
  <p class="lorem legend-item" style="top:50px;--c:var(--blue)">Lorem ipsum dolor sit amet, consectetur adipiscing elit. Aliquam odio nulla, blandit eu suscipit ac, pulvinar in mauris. Mauris ac sodales ante. Donec congue lectus vel libero facilisis luctus.</p>
  <p class="lorem legend-item" style="top:98px;--c:var(--orange)">Lorem ipsum dolor sit amet, consectetur adipiscing elit. Aliquam odio nulla, blandit eu suscipit ac, pulvinar in mauris. Mauris ac sodales ante. Donec congue lectus vel libero facilisis luctus.</p>
  <p class="lorem legend-item" style="top:146px;--c:#333">Lorem ipsum dolor sit amet, consectetur adipiscing elit. Aliquam odio nulla, blandit eu suscipit ac, pulvinar in mauris. Mauris ac sodales ante. Donec congue lectus vel libero facilisis luctus.</p>
  <footer class="footer"><span class="logo">logo</span><span class="rule"></span><span class="site">www.yourwebsite.com</span><span class="pager"><span class="next">Next</span><span>Previous</span></span></footer>
</section>

<!-- 13 Timeline -->
<section class="slide c1 r5">
  <h2 class="slide-title">Timeline</h2><p class="slide-sub">text &nbsp;for second title</p><span class="slide-num">11</span>
  <svg style="position:absolute;left:0;top:0" width="300" height="226" viewBox="0 0 300 226" font-family="Open Sans,sans-serif" font-size="8" text-anchor="middle">
    <line x1="10" y1="113" x2="290" y2="113" stroke="#c98a5a" stroke-width="1.2"/>
    <g fill="#e8772e"><circle cx="12" cy="113" r="2.5"/><circle cx="42" cy="113" r="2.5"/><circle cx="71" cy="113" r="2.5"/><circle cx="100" cy="113" r="2.5"/><circle cx="122" cy="113" r="2.5"/><circle cx="150" cy="113" r="2.5"/><circle cx="170" cy="113" r="2.5"/><circle cx="200" cy="113" r="2.5"/><circle cx="236" cy="113" r="2.5"/><circle cx="262" cy="113" r="2.5"/></g>
    <g fill="none" stroke-width=".8">
      <path d="M22 113V85M22 75V68h7" stroke="#faa54b"/><path d="M94 113V85M94 75V68h7" stroke="#faa54b"/><path d="M167 113V85M167 75V68h7" stroke="#888"/><path d="M229 113V85M229 75V68h7" stroke="#888"/>
      <path d="M44 113v15M44 150v12h6" stroke="#faa54b"/><path d="M113 113v15M113 150v12h6" stroke="#faa54b"/><path d="M184 113v15M184 150v12h6" stroke="#555"/><path d="M244 113v15M244 150v12h6" stroke="#888"/>
    </g>
    <g fill="#fff"><circle cx="22" cy="80" r="8" fill="#faa54b"/><text x="22" y="83">A</text><circle cx="94" cy="80" r="8" fill="#3277b5"/><text x="94" y="83">B</text><circle cx="167" cy="80" r="8" fill="#555"/><text x="167" y="83">C</text><circle cx="229" cy="80" r="8" fill="#bbb"/><text x="229" y="83">D</text>
      <circle cx="44" cy="139" r="8" fill="#faa54b"/><text x="44" y="142">a</text><circle cx="113" cy="139" r="8" fill="#3277b5"/><text x="113" y="142">b</text><circle cx="184" cy="139" r="8" fill="#555"/><text x="184" y="142">c</text><circle cx="244" cy="139" r="8" fill="#bbb"/><text x="244" y="142">d</text></g>
  </svg>
  <span class="tl-num o" style="left:31px;top:63px">501</span><span class="tl-num o" style="left:103px;top:63px">499</span><span class="tl-num" style="left:176px;top:63px">385</span><span class="tl-num" style="left:238px;top:63px">297</span>
  <p class="tl-text" style="left:31px;top:74px">Content here, making it look like readable</p>
  <p class="tl-text" style="left:103px;top:74px">Lorem Ipsum is that it has a more-or-less normal</p>
  <p class="tl-text" style="left:176px;top:74px">Distribution of letters, as opposed to publishing</p>
  <p class="tl-text" style="left:238px;top:74px">packages and you need to be sure there isn't anything</p>
  <p class="tl-text" style="left:34px;top:150px">Lorem dolor, adipiscing</p>
  <p class="tl-text" style="left:122px;top:150px">Established fact and web</p>
  <p class="tl-text" style="left:193px;top:150px">Readable content</p>
  <p class="tl-text" style="left:253px;top:150px">Consecter adipiscing</p>
  <span class="tl-num o" style="left:52px;top:168px">130</span><span class="tl-num o" style="left:121px;top:168px">184</span><span class="tl-num" style="left:192px;top:168px">319</span><span class="tl-num" style="left:252px;top:168px">276</span>
  <footer class="footer"><span class="logo">logo</span><span class="rule"></span><span class="site">www.yourwebsite.com</span><span class="pager"><span class="next">Next</span><span>Previous</span></span></footer>
</section>

<!-- 14 Thank you -->
<section class="slide c2 r5 thanks">
  <h2>THANK YOU</h2><span class="under"></span>
  <p class="contact" style="top:156px"><svg width="7" height="7" viewBox="0 0 10 10" fill="#fff"><path d="M2 0l2 2.5-1.2 1.4a6 6 0 0 0 3.3 3.3L7.5 6 10 8l-1.5 2C4 10 0 6 0 1.5z"/></svg>000-000-0000</p>
  <p class="contact" style="top:171px"><svg width="7" height="5" viewBox="0 0 10 7" fill="#fff"><rect width="10" height="7"/><path d="M0 0l5 4 5-4" stroke="#3277b5" fill="none"/></svg>xyz@email.com</p>
  <p class="contact" style="top:186px"><svg width="7" height="7" viewBox="0 0 10 10" fill="none" stroke="#fff" stroke-width="1.2"><circle cx="5" cy="5" r="4.2"/><path d="M1 5h8M5 1c2 2.5 2 5.5 0 8M5 1c-2 2.5-2 5.5 0 8"/></svg>www.yourwebsite.com</p>
  <div class="social" aria-label="Social links"><span></span><span></span><span></span></div>
</section>

</body>
</html>
```